Flyer redesign

We need this flier {Seasonal Care back 2018} redesigned for our 2019 season. It is attached below. New design should look different from current design. Be creative yet still professional.

Requirements
Must have
• Designed in photoshop.
• Should have the same text as current design. Only is "2019" instead of 2018. We want a different look with same info to send our customers next year.
• size: standard letter paper 8.5" x 11"
Nice to have
• Can use optional images provided. Not required though. See our website for more photos. thornbrookmemorial.org. send message through briskdrafts if you want a specific photo.
Should not have
• Do not take current design and just change date or image. Make the design look different.

```html
<!DOCTYPE html>
<html lang="en">
<head>
<meta charset="utf-8">
<title>2019 Gravesite Landscaping Packages</title>
<link href="https://fonts.googleapis.com/css2?family=Open+Sans:wght@400;700;800&family=Tinos:wght@400;700&display=swap" rel="stylesheet">
<style>
  :root{
    --maroon:#7d1f2f;
    --maroon-dark:#6a1826;
    --crimson:#b8304a;
    --sand:#e4dbaf;
    --cream:#f1ebc8;
    --butter:#f3e9a2;
    --ink:#3a3a3a;
    --page-bg:#ececec;
    --foliage:#6f9a4a;
    --foliage-dark:#3f6a2a;
  }
  *{box-sizing:border-box;margin:0;padding:0}
  html,body{width:1154px;height:1200px;overflow:hidden;background:var(--page-bg)}
  .flyer{position:absolute;left:129px;top:20px;width:896px;height:1160px;background:#fff;overflow:hidden;font-family:"Open Sans",Arial,sans-serif;color:var(--ink)}
  .hero-photo{position:absolute;left:0;top:0;width:896px;height:400px;background:linear-gradient(180deg,#9cc27a 0%,var(--foliage) 45%,var(--foliage-dark) 100%)}
  .title-box{position:absolute;left:20px;top:20px;width:250px;height:290px;background:var(--maroon);color:#fff;text-align:center;font-family:"Tinos",serif;padding-top:18px}
  .title-year{font-size:92px;line-height:1;letter-spacing:1px}
  .title-text{font-size:36px;line-height:1.18;margin-top:6px}
  .waves{position:absolute;left:0;top:230px;width:896px;height:200px}
  .column{position:absolute;top:430px;text-align:center;padding:0 18px}
  .col-seasonal{left:60px;width:220px;height:570px;background:linear-gradient(180deg,var(--sand) 0%,var(--sand) 72%,#fff 100%)}
  .col-basic{left:300px;width:250px;height:570px;background:linear-gradient(180deg,var(--cream) 0%,var(--cream) 72%,#fff 100%)}
  .col-perpetual{left:570px;width:270px;height:640px;background:linear-gradient(180deg,var(--butter) 0%,var(--butter) 82%,#fff 100%)}
  .col-head{height:110px;padding-top:30px}
  .col-title{font-weight:800;font-size:19px;line-height:1.2;color:var(--maroon);text-transform:uppercase}
  .col-sub{font-size:13.5px;line-height:1.35;color:var(--crimson);margin-top:4px}
  .chevron{display:block;width:calc(100% + 36px);margin:0 -18px;height:50px}
  .features{list-style:none;text-align:left;font-size:13px;line-height:1.3;margin-top:14px}
  .features li{position:relative;padding-left:18px;margin-bottom:7px}
  .features li svg{position:absolute;left:0;top:3px;width:12px;height:12px}
  .price-label{font-family:"Tinos",serif;font-weight:700;color:var(--maroon);font-size:20px;line-height:1.1;text-transform:uppercase}
  .price{font-family:"Tinos",serif;font-weight:700;color:var(--maroon);font-size:36px;line-height:1}
  .tier{margin-top:12px}
  .fine{font-family:"Tinos",serif;font-size:12.5px;line-height:1.3;margin-top:12px}
  .badge{position:absolute;left:610px;top:1010px;width:240px;height:50px;background:var(--crimson);color:#fff;font-family:"Tinos",serif;font-size:23px;line-height:50px;text-align:center;letter-spacing:1px;clip-path:polygon(5% 0,100% 0,100% 100%,5% 100%,0 50%)}
  .brand{position:absolute;left:40px;top:1012px;width:520px;height:64px;display:flex;align-items:center;justify-content:center;gap:16px;font-family:"Tinos",serif;font-size:36px;line-height:1;color:var(--maroon);font-variant:small-caps}
  .brand-dot{width:16px;height:16px;border-radius:50%;background:var(--maroon)}
  .footer{position:absolute;left:0;top:1090px;width:896px;height:70px;background:var(--maroon);color:#fff;font-family:"Tinos",serif;font-size:21px;display:flex;align-items:center;justify-content:center;gap:26px}
  .footer .sep{width:2px;height:30px;background:#fff}
</style>
</head>
<body>
<main class="flyer">
  <div class="hero-photo" role="img" aria-label="Photo of a tree-shaded cemetery lawn with headstones and trimmed hedges"></div>

  <svg class="waves" viewBox="0 0 896 200" preserveAspectRatio="none" aria-hidden="true">
    <path d="M0 40 Q300 150 896 150 L896 200 L0 200 Z" fill="var(--maroon-dark)"/>
    <path d="M0 70 Q250 130 620 150 L896 150 L896 190 L0 190 Z" fill="var(--crimson)"/>
    <path d="M0 120 Q300 150 896 165 L896 200 L0 200 Z" fill="var(--maroon)"/>
  </svg>

  <header class="title-box">
    <div class="title-year">2019</div>
    <div class="title-text">Gravesite<br>Landscaping<br>Packages</div>
  </header>

  <section class="column col-seasonal">
    <div class="col-head">
      <h2 class="col-title">Seasonal<br>Care</h2>
      <p class="col-sub">Seasonal landscaping<br>grave care.</p>
    </div>
    <svg class="chevron" viewBox="0 0 100 30" preserveAspectRatio="none" aria-hidden="true"><path d="M0 0 L50 22 L100 0 L100 8 L50 30 L0 8 Z" fill="var(--maroon)"/></svg>
    <ul class="features">
      <li><svg viewBox="0 0 12 12"><circle cx="6" cy="6" r="5" fill="none" stroke="var(--ink)"/><path d="M3 6 L5.3 8.2 L9.5 3" fill="none" stroke="var(--ink)" stroke-width="1.5"/></svg>Weeding and trimming services on your gravesite approximately every 7 weeks during the growing season: mid-April through mid-October</li>
    </ul>
    <div class="tier"><div class="price-label">3 Years</div><div class="price">$327</div></div>
    <div class="tier"><div class="price-label">2 Years</div><div class="price">$218</div></div>
    <div class="tier"><div class="price-label">1 Year</div><div class="price">$109</div></div>
    <p class="fine">Multi-year payment<br>locks in current rates.</p>
  </section>

  <section class="column col-basic">
    <div class="col-head">
      <h2 class="col-title">Basic Care<br>Endowment</h2>
      <p class="col-sub">Landscaping care forever<br>for graves with no plantings.</p>
    </div>
    <svg class="chevron" viewBox="0 0 100 30" preserveAspectRatio="none" aria-hidden="true"><path d="M0 0 L50 22 L100 0 L100 8 L50 30 L0 8 Z" fill="var(--maroon)"/></svg>
    <ul class="features">
      <li><svg viewBox="0 0 12 12"><circle cx="6" cy="6" r="5" fill="none" stroke="var(--ink)"/><path d="M3 6 L5.3 8.2 L9.5 3" fill="none" stroke="var(--ink)" stroke-width="1.5"/></svg>Weeding and trimming services on your gravesite 2 times per year: mid-May and mid-September</li>
      <li><svg viewBox="0 0 12 12"><circle cx="6" cy="6" r="5" fill="none" stroke="var(--ink)"/><path d="M3 6 L5.3 8.2 L9.5 3" fill="none" stroke="var(--ink)" stroke-width="1.5"/></svg>Monument leveling</li>
      <li><svg viewBox="0 0 12 12"><circle cx="6" cy="6" r="5" fill="none" stroke="var(--ink)"/><path d="M3 6 L5.3 8.2 L9.5 3" fill="none" stroke="var(--ink)" stroke-width="1.5"/></svg>Payment ensures grave care forever</li>
    </ul>
    <div class="tier"><div class="price-label">12 Monthly<br>Payments of</div><div class="price">$225.00*</div></div>
    <p class="fine">*gravesites with single headstones.<br>Call for other monument types and single payment discount. Valid through 10/31/19.</p>
  </section>

  <section class="column col-perpetual">
    <div class="col-head">
      <h2 class="col-title">Perpetual Care<br>Endowment</h2>
      <p class="col-sub">Landscaping care forever<br>for graves with plantings.</p>
    </div>
    <svg class="chevron" viewBox="0 0 100 30" preserveAspectRatio="none" aria-hidden="true"><path d="M0 0 L50 22 L100 0 L100 8 L50 30 L0 8 Z" fill="var(--maroon)"/></svg>
    <ul class="features">
      <li><svg viewBox="0 0 12 12"><circle cx="6" cy="6" r="5" fill="none" stroke="var(--ink)"/><path d="M3 6 L5.3 8.2 L9.5 3" fill="none" stroke="var(--ink)" stroke-width="1.5"/></svg>Weeding and trimming services on your gravesite approximately every 7 weeks during the growing season: mid-April through mid-October</li>
      <li><svg viewBox="0 0 12 12"><circle cx="6" cy="6" r="5" fill="none" stroke="var(--ink)"/><path d="M3 6 L5.3 8.2 L9.5 3" fill="none" stroke="var(--ink)" stroke-width="1.5"/></svg>Monument leveling and cleaning</li>
      <li><svg viewBox="0 0 12 12"><circle cx="6" cy="6" r="5" fill="none" stroke="var(--ink)"/><path d="M3 6 L5.3 8.2 L9.5 3" fill="none" stroke="var(--ink)" stroke-width="1.5"/></svg>Payment ensures grave care forever</li>
      <li><svg viewBox="0 0 12 12"><circle cx="6" cy="6" r="5" fill="none" stroke="var(--ink)"/><path d="M3 6 L5.3 8.2 L9.5 3" fill="none" stroke="var(--ink)" stroke-width="1.5"/></svg>Full bed of boxwood shrubs</li>
      <li><svg viewBox="0 0 12 12"><circle cx="6" cy="6" r="5" fill="none" stroke="var(--ink)"/><path d="M3 6 L5.3 8.2 L9.5 3" fill="none" stroke="var(--ink)" stroke-width="1.5"/></svg>Replacement of shrubs</li>
      <li><svg viewBox="0 0 12 12"><circle cx="6" cy="6" r="5" fill="none" stroke="var(--ink)"/><path d="M3 6 L5.3 8.2 L9.5 3" fill="none" stroke="var(--ink)" stroke-width="1.5"/></svg>Trust certificate</li>
    </ul>
    <div class="tier"><div class="price-label">12 Monthly<br>Payments of</div><div class="price">$280.42</div></div>
    <p class="fine">Call for payment discount.<br>Valid through 10/31/19</p>
  </section>

  <div class="badge">MOST POLPULAR</div>

  <div class="brand"><span class="brand-dot"></span>Thornbrook Memorial</div>

  <footer class="footer">
    <span>info@thornbrookmemorial.org</span><span class="sep"></span>
    <span>(201) 555-0148</span><span class="sep"></span>
    <span>www.thornbrookmemorial.org</span>
  </footer>
</main>
</body>
</html>
```